Granite, Zinc and Clay Roofing LLC needs a new business card

I need a new business card because I have a new address.
I do slate copper and tile roofs. My webpage is: www.granitezincandclayroofing.example

```html
<!DOCTYPE html>
<html lang="en">
<head>
<meta charset="utf-8">
<title>Granite, Zinc and Clay Roofing LLC — Business Card</title>
<link href="https://fonts.googleapis.com/css2?family=Arimo:wght@400;700&display=swap" rel="stylesheet">
<style>
  :root {
    --stage: #2b2b2b;
    --card-blue: #519fcf;
    --ink: #000000;
    --paper: #ffffff;
  }
  * { margin: 0; padding: 0; box-sizing: border-box; }
  html, body { width: 1200px; height: 1015px; overflow: hidden; }
  body {
    background: var(--stage);
    font-family: "Arimo", Arial, sans-serif;
    color: var(--ink);
    position: relative;
  }
  .card {
    position: absolute;
    width: 560px;
    height: 320px;
    overflow: hidden;
    box-shadow: 0 10px 30px rgba(0,0,0,.5);
  }
  .card-front {
    left: 60px; top: 110px;
    background: var(--card-blue);
    display: flex; align-items: center; justify-content: center;
  }
  .brand-mark { display: flex; align-items: center; gap: 14px; }
  .brand-square { width: 34px; height: 34px; background: var(--ink); flex: none; }
  .brand-name { font-size: 24px; font-weight: 700; line-height: 1.15; color: var(--ink); }

  .card-back {
    left: 580px; top: 585px;
    background: var(--card-blue);
  }
  .back-shape { position: absolute; inset: 0; }
  .back-brand { position: absolute; left: 318px; top: 62px; width: 225px; }
  .back-brand.brand-mark { gap: 10px; }
  .back-brand .brand-square { width: 22px; height: 22px; }
  .back-brand .brand-name { font-size: 17px; }

  .contact { position: absolute; left: 40px; top: 50px; }
  .person-name { font-size: 20px; font-weight: 700; }
  .person-role { font-size: 14px; margin-top: 2px; }
  .address { font-size: 14px; line-height: 1.3; margin-top: 40px; }
  .reach { list-style: none; margin-top: 36px; font-size: 13px; line-height: 1.55; }
  .reach li { display: flex; align-items: center; gap: 8px; }
  .reach svg { width: 13px; height: 13px; flex: none; }
</style>
</head>
<body>

<section class="card card-front" aria-label="Card front">
  <div class="brand-mark">
    <span class="brand-square"></span>
    <span class="brand-name">Granite, Zinc and Clay<br>Roofing LLC</span>
  </div>
</section>

<section class="card card-back" aria-label="Card back">
  <svg class="back-shape" viewBox="0 0 560 320" aria-hidden="true">
    <circle cx="472" cy="66" r="220" fill="var(--ink)"/>
    <circle cx="480" cy="60" r="220" fill="var(--paper)"/>
  </svg>

  <div class="brand-mark back-brand">
    <span class="brand-square"></span>
    <span class="brand-name">Granite, Zinc and Clay<br>Roofing LLC</span>
  </div>

  <div class="contact">
    <p class="person-name">Laszlo (Les) Varga</p>
    <p class="person-role">Owner</p>
    <p class="address">2870 Millbrook Rd.<br>Fairview, OH 44099</p>
    <ul class="reach">
      <li>
        <svg viewBox="0 0 24 24"><path fill="currentColor" d="M6.6 10.8a15 15 0 0 0 6.6 6.6l2.2-2.2c.3-.3.7-.4 1-.2 1.1.4 2.3.6 3.6.6.6 0 1 .4 1 1V20c0 .6-.4 1-1 1A17 17 0 0 1 3 4c0-.6.4-1 1-1h3.5c.6 0 1 .4 1 1 0 1.3.2 2.5.6 3.6.1.3 0 .7-.2 1z"/></svg>
        (440)555-0187
      </li>
      <li>
        <svg viewBox="0 0 24 24" fill="none" stroke="currentColor" stroke-width="2"><circle cx="12" cy="12" r="10"/><path d="M2 12h20M12 2c3 3 3 17 0 20M12 2c-3 3-3 17 0 20"/></svg>
        www.granitezincandclayroofing.example
      </li>
      <li>
        <svg viewBox="0 0 24 24" fill="none" stroke="currentColor" stroke-width="2"><rect x="2" y="5" width="20" height="14"/><path d="M2 5l10 8 10-8"/></svg>
        office@granitezincclay.example
      </li>
    </ul>
  </div>
</section>

</body>
</html>
```